Web Design Project

I need designs (PSD only - no programming) for several pages of a new website helping train operators to manage key information about their traindrivers.
The main feature of this website is the management of personnel records (create, edit, search, delete). Another key aspect is the management of user privileges. Since this is a new website we also need a user friendly frontpage, pricing information and how it works sections.
This can be broken down into 9 pages for which we need designs (PSDs).
1. Home
2. Driver record
3. How it works
4. Pricing
5. User administration
6. Help
7. Record list view
8. Login
9. Registration
Navigation (not logged in) are: Home | How it works | Pricing | Customers | About us | Contact
Navigation (logged in) are: Overview | Administration | Manage records | Billing | Help | Contact
Footer: Customer logos | Awards | Terms & Conditions | Privacy
To provide the best support for you to come up with a strong design proposal I will provide DAILY feedback to all participants. We have also created concept mockups (attached) and example pages (below) for each section to give you a clear sense of what we look for.
The core concepts for a successful bid are that the website is EASY to understand, INTUITIVE to navigate, and SIMPLE to use. Most of our users lack technical background and are looking for tool to simplify their work.
The strongest participants (winner and close contenders) will have the opportunity to additional commissioned work on additional sections not included in this brief.
Example Pages (by section)
1. http://www.brovendale.example/site-keepers/
1. http://www.qvt.example/
1. http://www.mondaph.example/
1. http://www.gorvanquest.example/
2. http://www.snapveld.example/profile_edit.gne
3. https://www.tarn.example/how-it-works/
3. http://www.bulkvue.example/learn
4. http://www.pactheron.example/crm/editions-pricing.jsp
4. http://www.brovendale.example/site-keepers/prices
6. https://support.talvora.example/en-gb/
6. http://help.dealmeadow.example/contact_us
8. https://www.careweave.example/uas/login
8. https://www.dealmeadow.example/login
8. http://www.askhollow.example/login/index
For form designs we like Verindo, Bidnook, Snapveld, CareWeave, Chatterly and the concepts presented by Tomas Kerrigan in his classic Layout Craft Shaping the Input Boxes.
For additional guidance see mockups attached!
Target Market(s)
Security, human resources and admin support employees for train operators.
Industry/Entity Type
Learn
Requirements
Should not have
- Home page should not have
Social media icons (chatterly, chirpla, CareWeave, RSS feed)
Contact forms
Read more links
Old trains

```html
<!DOCTYPE html>
<html lang="en">
<head>
<meta charset="utf-8">
<title>CredRail – Home</title>
<link rel="stylesheet" href="https://fonts.googleapis.com/css2?family=Arimo:wght@400;700&display=swap">
<style>
  :root {
    --sky: #45b8d5;
    --sky-deep: #2fa3c3;
    --sky-light: #6fcbe2;
    --ink: #111111;
    --night: #050505;
    --paper: #ffffff;
    --mist: #ededed;
    --rule: #b9b9b9;
    --slate: #a9a9a9;
    --nav-active: #3cb3d6;
    --signal-red: #e5262b;
    --signal-yellow: #f2d21a;
  }
  * { box-sizing: border-box; margin: 0; padding: 0; }
  html, body { width: 1200px; height: 2246px; overflow: hidden; }
  body {
    position: relative;
    font-family: "Arimo", Arial, sans-serif;
    background: var(--sky);
    color: var(--ink);
  }
  .abs { position: absolute; }

  /* utility bar */
  .utility-bar {
    left: 0; top: 0; width: 1200px; height: 34px;
    background: var(--night);
    border-top: 7px solid var(--sky);
  }
  .utility-links {
    right: 22px; top: 8px;
    color: var(--paper); font-size: 13px;
  }

  /* header */
  .site-header {
    left: 0; top: 34px; width: 1200px; height: 125px;
    background: linear-gradient(#ffffff, #f1f1f1 60%, #dcdcdc);
  }
  .brand {
    left: 30px; top: 32px;
    display: flex; align-items: center; gap: 10px;
    font-size: 40px; color: #2a6fa8; font-weight: 400;
  }
  .brand-dot { width: 18px; height: 18px; border-radius: 50%; background: var(--signal-red); }
  .main-nav {
    left: 527px; top: 78px;
    font-size: 22px; color: var(--ink); white-space: nowrap;
  }
  .main-nav .current { color: var(--nav-active); }
  .nav-pointer { left: 538px; top: 145px; }

  /* slider */
  .slider-frame {
    left: 176px; top: 189px; width: 846px; height: 335px;
    background: linear-gradient(100deg, #1b1d22 0%, #5d7f9e 30%, #c9c3b4 55%, #efe0a8 75%, #6a6253 100%);
  }
  .slider-caption {
    left: 648px; top: 296px; width: 374px; height: 152px;
    background: rgba(205,205,205,0.75);
    font-size: 36px; line-height: 36px; color: var(--ink);
    padding: 22px 16px 0 0; text-align: right;
  }
  .slider-caption span { display: block; }
  .slider-caption .l1 { margin-right: 124px; }
  .slider-caption .l2 { margin-right: 60px; }
  .slider-arrow { top: 298px; }
  .slider-dots { left: 468px; top: 538px; display: flex; gap: 15px; }
  .slider-dots i {
    width: 24px; height: 24px; border-radius: 50%;
    background: #d8d8d8; box-shadow: inset 0 -2px 3px rgba(0,0,0,0.15);
  }
  .slider-dots i.on { background: #9a9a9a; box-shadow: inset 0 2px 4px rgba(0,0,0,0.4); }

  /* quote band */
  .quote-band {
    left: 0; top: 577px; width: 1200px; height: 74px;
    background: var(--night); color: var(--paper);
    font-size: 22px; text-align: center; line-height: 74px;
  }

  /* content panel */
  .content-panel {
    left: 24px; top: 683px; width: 1148px; height: 1442px;
    background: var(--paper);
    box-shadow: 0 0 22px rgba(0,0,0,0.35);
  }
  .section-tab {
    left: 19px; width: 277px;
    background: linear-gradient(var(--sky-light), var(--sky) 50%, var(--sky-deep));
    border-left: 8px solid #8fdcef;
    color: var(--paper); font-size: 40px;
    box-shadow: 3px 4px 8px rgba(0,0,0,0.45);
    display: flex; align-items: center; justify-content: center;
  }
  .benefits-tab { top: 726px; height: 85px; }
  .how-tab { top: 1275px; height: 92px; }

  .body-copy {
    font-size: 20px; line-height: 26.5px; text-align: justify; color: var(--ink);
  }
  .benefits-left { left: 88px; top: 795px; width: 595px; }
  .benefits-left .lead { text-indent: 234px; }
  .benefits-left .fine { font-size: 13px; line-height: 16px; margin-top: 6px; }
  .benefits-right { left: 721px; top: 794px; width: 375px; }

  .cta-button {
    width: 240px; height: 44px; border-radius: 7px;
    background: linear-gradient(#5cc7e2, var(--sky-deep));
    box-shadow: 0 2px 4px rgba(0,0,0,0.45);
    color: var(--paper); font-size: 20px; text-align: center; line-height: 44px;
  }
  .cta-button .signup { color: var(--signal-red); }
  .cta-button .call { color: var(--signal-yellow); }
  .cta-benefits { left: 852px; top: 1155px; }
  .cta-how { left: 856px; top: 1634px; }

  .section-rule { left: 24px; top: 1229px; width: 1148px; height: 2px; background: var(--rule); }

  .presenter-photo {
    left: 37px; top: 1393px; width: 460px; height: 325px;
    background: radial-gradient(ellipse at 40% 45%, #e9d9cc 0%, #f4f1ee 55%, #ffffff 80%);
  }
  .how-copy { left: 350px; top: 1296px; width: 750px; }
  .how-copy p { text-indent: 24px; }

  .train-photo {
    left: 24px; top: 1718px; width: 1148px; height: 210px;
    background: linear-gradient(90deg, #2b2f34 0%, #5a6066 35%, #d9dcde 55%, #f2f2f2 70%, #4a4e52 100%);
  }

  .partner-logo {
    top: 1988px; width: 120px; height: 86px; background: var(--slate);
  }

  /* footer */
  .footer-nav {
    left: 0; top: 2154px; width: 1200px; text-align: center;
    color: var(--paper); font-size: 22px;
  }
  .legal-bar {
    left: 0; top: 2209px; width: 1200px; height: 37px;
    background: var(--night); color: var(--paper);
    font-size: 14px; text-align: center; line-height: 37px;
  }
</style>
</head>
<body>

  <div class="abs utility-bar"></div>
  <div class="abs utility-links">Signup | Login | Language(English)</div>

  <header class="abs site-header"></header>
  <div class="abs brand"><span class="brand-dot"></span><span>CredRail</span></div>
  <nav class="abs main-nav"><span class="current">Home</span> | How it Works | Prices | Our Customers | About Us | Contact</nav>
  <svg class="abs nav-pointer" width="24" height="14" viewBox="0 0 24 14"><path d="M0 14 L12 2 L24 14 Z" fill="#45b8d5"/></svg>

  <div class="abs slider-frame" role="img" aria-label="Photo of a high-speed train blurred with motion along rail tracks at sunset"></div>
  <div class="abs slider-caption">
    <span class="l1">Lorem ipsum</span>
    <span class="l2">Lorem ipsum</span>
    <span>Lorem ipsum</span>
  </div>
  <svg class="abs slider-arrow" style="left:74px" width="78" height="120" viewBox="0 0 78 120">
    <path d="M6 6 L72 60 L6 114 L6 86 L40 60 L6 34 Z" fill="#d0d0d0" stroke="#a8a8a8" stroke-width="2"/>
  </svg>
  <svg class="abs slider-arrow" style="left:1054px" width="78" height="120" viewBox="0 0 78 120">
    <path d="M72 6 L6 60 L72 114 L72 86 L38 60 L72 34 Z" fill="#d0d0d0" stroke="#a8a8a8" stroke-width="2"/>
  </svg>
  <div class="abs slider-dots"><i></i><i></i><i class="on"></i><i></i><i></i><i></i><i></i></div>

  <div class="abs quote-band">“Lorem ipsum dolor sit amet, consectetur adipiscing elit. Etiam tristique feugiat enim.”</div>

  <main class="abs content-panel"></main>

  <h2 class="abs section-tab benefits-tab">Benefits</h2>
  <div class="abs body-copy benefits-left">
    <p class="lead">Lorem ipsum dolor sit amet, consectetur adipiscing elit. Etiam tristique feugiat enim, et porta enim commodo sit amet. Aliquam erat volutpat. Suspendisse potenti. Vivamus sed ligula massa, a vulputate dolor. Fusce ac tellus quam, sit amet lobortis elit. Aenean tempor faucibus faucibus. Nunc condimentum mattis &nbsp;llus condimentum rhoncus quam, non convallis velit consequat a. Quisque blandit porttitor semper. Sed eu ipsum ligula, ac condimentum purus. Mauris at massa eros.</p>
    <p class="fine">“Lorem ipsum dolor sit amet, consectetur adipiscing elit. Etiam tristique feugiat enim, et porta enim commodo sit amet. Aliquam erat volutpat. Suspendisse potenti. Vivamus sed ligula massa, a vulputate dolor. Fusce ac tellus quam, sit amet lobortis elit. Aenean tempor faucibus faucibus. Nunc condimentum mattis &nbsp;llus condimentum rhoncus quam, non convallis velit consequat a. Quisque blandit porttitor semper. Sed eu ipsum ligula, ac condimentum purus. Mauris at massa eros.”</p>
  </div>
  <div class="abs body-copy benefits-right">
    <p>Lorem ipsum dolor sit amet, consectetur adipiscing elit. Etiam tristique feugiat enim, et porta enim commodo sit amet. Aliquam erat volutpat. Suspendisse potenti. Vivamus sed ligula massa, a vulputate dolor. Fusce ac tellus quam, sit amet lobortis elit. Aenean tempor faucibus faucibus. Nunc condimentum mattis &nbsp;llus condimentum rhoncus quam, non convallis velit consequat a. Quisque blandit porttitor semper. Sed eu ipsum ligula, ac condimentum purus. Mauris at massa eros.</p>
  </div>
  <div class="abs cta-button cta-benefits"><span class="signup">Signup</span> or request a <span class="call">Call</span></div>

  <div class="abs section-rule"></div>

  <h2 class="abs section-tab how-tab">How it Works</h2>
  <div class="abs presenter-photo" role="img" aria-label="Photo of a smiling woman in a white shirt presenting with an open hand"></div>
  <div class="abs body-copy how-copy">
    <p>Lorem ipsum dolor sit amet, consectetur adipiscing elit. Etiam tristique feugiat enim, et porta enim commodo sit amet. Aliquam erat volutpat. Suspendisse potenti. Vivamus sed ligula massa, a vulputate dolor. Fusce ac tellus quam, sit amet lobortis elit. Aenean tempor faucibus faucibus. Nunc condimentum mattis &nbsp;llus condimentum rhoncus quam, non convallis velit consequat a. Quisque blandit porttitor semper. Sed eu ipsum ligula, ac condimentum purus. Mauris at massa eros.</p>
    <p>Nunc condimentum mattis &nbsp;llus condimentum rhoncus quam, non convallis velit consequat a. Quisque blandit porttitor semper. Sed eu ipsum ligula, ac condimentum purus. Mauris at massa eros.</p>
  </div>
  <div class="abs cta-button cta-how"><span class="signup">Signup</span> or request a <span class="call">Call</span></div>

  <div class="abs train-photo" role="img" aria-label="Photo of a white high-speed train waiting at a station platform"></div>

  <div class="abs partner-logo" style="left:125px" role="img" aria-label="Partner badge"></div>
  <div class="abs partner-logo" style="left:290px" role="img" aria-label="Partner badge"></div>
  <div class="abs partner-logo" style="left:453px" role="img" aria-label="Partner badge"></div>

  <nav class="abs footer-nav">Home | How it Works | Prices | Our Customers | About Us | Contact</nav>
  <footer class="abs legal-bar">Copyright &nbsp; 2012 CredRail | All right reserved | T&amp;C</footer>

</body>
</html>
```